Business Card Design Needed for Landscaping & Trail Building Company

We need a business card for our landscaping and trail-building business using our current artwork (attached). We build mountain bike trails and pump tacks along with our base business - landscaping - which is primarily earth moving, machine work, concreting, retaining walls, paths, etc. for commercial and residential customers. We want a design that is professional, sleek, and earthy. We like clean, open space (i.e. logo artwork only, on one side, with pertinent information on the back) and a somewhat ambiguous look considering our varied clientele between the trail work and the landscape work.

Target Market(s)

Ski resort executives. government employees (rangers, council members, etc), average homeowner, other tradies, builders, etc.

Contact Information for Business Card

Must include the following:
employee name: Marcus
mobile number: 0437 615 920
email: marcus@brelloway.com.au
website: brelloway.com.au
ABN: 58 314 962 807
NTWA: 27493516
^This is the Northgate Trade & Works Authority license number, a requirement to be displayed on promotional material for our state
Description of services: "Residential and commercial landscaping, minor earth works and trail building"

Font styles to use
Serif

Colors
ffc214
9bcb3c
333333
0355a3

Requirements
Must have
• Please see "Business Card Details" as these are all the pieces of information required to be on there. This will be a slim card, so the final size needs to be 45mm x 90mm, landscape perspective.
• I will include the requirements of our printer below:
• File Format
• PDF files
• CMYK colour
• 300dpi resolution minimum
• Fonts converted to outlines or flattened
• Resolution
• Images such as photos in your artwork must have a minimum resolution of 300dpi. Images that have a lower resolution may print pixelated or fuzzy. Images taken from the internet often have a resolution of only 72dpi and will very rarely print very well.
• Correct Colour
• Digital printing uses a CMYK colour format (Cyan, Magenta, Yellow and Black). The colours on your screen are RGB colours (Red, Green, Blue).
• Some RGB colours that appear on your screen can not be printed in CMYK. You must be careful when selecting colours for your printing, as some colours will print "dull" when compared to your computer screen.
• Programs such as Adobe Photoshop and Adobe Illustrator can convert all colours to CMYK. Programs such as Microsoft Word can not, so you must manually select colours which are not at risk.
• Fonts
• You may choose to select only common fonts such as "Arial" and "Times New Roman", or you can "embed" the fonts when saving your artwork. Preferably fonts in your artwork need to be "converted to outlines" or "flattened" into a graphic. This will eliminate the chance of fonts not displaying correctly and not printing the way you intended.
• Business Card Artwork Size
• 94mm x 59mm (including 2mm bleed)
• Artwork Bleeds - IMPORTANT!
• Your artwork needs to be a certain size to print correctly. For business cards it is 94mmx59mm. Part of this size is what we call the "bleed" which will be trimmed off. The bleed area is 2mm on each side. In addition to the bleed area outside the cut line, we strongly recommend making another internal margin as the cut line can vary in location.
Nice to have
• We will have a print run of two designs, one with my details (Dana) and one with Marcus's.
• (I like the idea of the name being larger than everything else, jumping out)
• The background colours we are interested in: very dark navy blue (almost black), fluorescent orange and green (same colour palette as our current artwork), and possibly black. The rest of the colour theming should match our current artwork. We will likely be printing these out in matte/soft finish with a gloss spot accent on the logo.
• I have attached the front/back of an example business card that we both like the look of.
• As a side note, we are open to creative designs that design outside of our specified preferences, as we have been blown away in the past by the creativity of designers.

```html
<!DOCTYPE html>
<html lang="en">
<head>
<meta charset="utf-8">
<title>Brelloway Business Card</title>
<link href="https://fonts.googleapis.com/css2?family=Cinzel:wght@600;700&family=Tinos:wght@400;700&family=Arimo&display=swap" rel="stylesheet">
<style>
  :root {
    --navy-deep: #151f33;
    --navy-mid: #172a48;
    --navy-blue: #0b4f8c;
    --leaf: #8dc63f;
    --sun: #f0a032;
    --sun-bright: #ffc214;
    --paper: #ffffff;
    --label: #222222;
  }
  * { box-sizing: border-box; margin: 0; padding: 0; }
  html, body {
    width: 724px; height: 1200px; overflow: hidden;
    background: var(--paper);
  }
  .sheet { position: relative; width: 724px; height: 1200px; }
  .side-label {
    position: absolute; left: 0; width: 724px; text-align: center;
    font-family: "Arimo", Arial, sans-serif; font-size: 24px; color: var(--label);
  }
  .side-label--front { top: -4px; }
  .side-label--back { top: 418px; }
  .card {
    position: absolute; left: 0; width: 724px; height: 361px;
    background: linear-gradient(115deg, var(--navy-deep) 0%, var(--navy-mid) 55%, var(--navy-blue) 100%);
    overflow: hidden;
  }
  .card--front { top: 38px; }
  .card--marcus { top: 453px; }
  .card--dana { top: 838px; }

  .brand {
    position: absolute; left: 0; width: 724px; top: 140px;
    display: flex; justify-content: center; align-items: center; gap: 18px;
  }
  .brand__dot {
    width: 96px; height: 96px; border-radius: 50%; background: var(--leaf);
  }
  .brand__name {
    font-family: "Cinzel", "Times New Roman", serif; font-weight: 700;
    font-size: 54px; color: var(--leaf); letter-spacing: 1px;
  }
  .services {
    position: absolute; left: 0; width: 724px; top: 277px; text-align: center;
    font-family: "Cinzel", "Times New Roman", serif; font-weight: 600;
    font-size: 20px; line-height: 29px; letter-spacing: 2px; color: var(--leaf);
  }

  .registration {
    position: absolute; left: 48px; top: 40px;
    font-family: "Tinos", "Times New Roman", serif; font-size: 22px;
    line-height: 25px; color: var(--paper);
  }
  .back-brand {
    position: absolute; right: 46px; top: 36px; width: 134px;
    display: flex; flex-direction: column; align-items: center; gap: 8px;
  }
  .back-brand__dot { width: 112px; height: 112px; border-radius: 50%; background: var(--leaf); }
  .back-brand__name {
    font-family: "Cinzel", "Times New Roman", serif; font-weight: 700;
    font-size: 18px; color: var(--leaf);
  }
  .person {
    position: absolute; left: 53px; top: 189px;
    font-family: "Tinos", "Times New Roman", serif; font-weight: 700;
    font-size: 32px; color: var(--sun);
  }
  .contacts {
    position: absolute; left: 48px; top: 240px; list-style: none;
    font-family: "Tinos", "Times New Roman", serif; font-size: 24px; color: var(--paper);
  }
  .contacts li { display: flex; align-items: center; height: 31px; }
  .contacts li:first-child { height: 34px; font-size: 25px; }
  .contacts svg { width: 22px; height: 22px; margin-right: 14px; flex: none; }
</style>
</head>
<body>
<div class="sheet">
  <div class="side-label side-label--front">Front</div>
  <section class="card card--front">
    <div class="brand">
      <span class="brand__dot"></span>
      <span class="brand__name">Brelloway</span>
    </div>
    <p class="services">Residential and commercial landscaping,<br>minor earth works and trail building</p>
  </section>

  <div class="side-label side-label--back">Back</div>

  <section class="card card--marcus">
    <p class="registration">ABN: 58 314 962 807<br>NTWA: 27493516</p>
    <div class="back-brand"><span class="back-brand__dot"></span><span class="back-brand__name">Brelloway</span></div>
    <h2 class="person">Marcus</h2>
    <ul class="contacts">
      <li><svg viewBox="0 0 22 22"><rect x="5" y="1" width="12" height="20" rx="3" fill="var(--leaf)"/><rect x="7.5" y="4" width="7" height="11" fill="var(--navy-deep)"/></svg>0437 615 920</li>
      <li><svg viewBox="0 0 22 22"><rect x="1" y="5" width="20" height="13" fill="var(--leaf)"/><path d="M1 5 L11 13 L21 5 M1 18 L8 11 M21 18 L14 11" stroke="var(--navy-deep)" stroke-width="1.4" fill="none"/></svg>marcus@brelloway.com.au</li>
      <li><svg viewBox="0 0 22 22"><circle cx="11" cy="11" r="9.5" fill="var(--leaf)"/><g stroke="var(--navy-deep)" stroke-width="1.3" fill="none"><ellipse cx="11" cy="11" rx="4" ry="9.5"/><path d="M1.5 11 H20.5 M3 6.5 H19 M3 15.5 H19 M11 1.5 V20.5"/></g></svg>brelloway.com.au</li>
    </ul>
  </section>

  <section class="card card--dana">
    <p class="registration">ABN: 58 314 962 807<br>NTWA: 27493516</p>
    <div class="back-brand"><span class="back-brand__dot"></span><span class="back-brand__name">Brelloway</span></div>
    <h2 class="person">Dana</h2>
    <ul class="contacts">
      <li><svg viewBox="0 0 22 22"><rect x="5" y="1" width="12" height="20" rx="3" fill="var(--leaf)"/><rect x="7.5" y="4" width="7" height="11" fill="var(--navy-deep)"/></svg>0437 615 920</li>
      <li><svg viewBox="0 0 22 22"><rect x="1" y="5" width="20" height="13" fill="var(--leaf)"/><path d="M1 5 L11 13 L21 5 M1 18 L8 11 M21 18 L14 11" stroke="var(--navy-deep)" stroke-width="1.4" fill="none"/></svg>dana@brelloway.com.au</li>
      <li><svg viewBox="0 0 22 22"><circle cx="11" cy="11" r="9.5" fill="var(--leaf)"/><g stroke="var(--navy-deep)" stroke-width="1.3" fill="none"><ellipse cx="11" cy="11" rx="4" ry="9.5"/><path d="M1.5 11 H20.5 M3 6.5 H19 M3 15.5 H19 M11 1.5 V20.5"/></g></svg>brelloway.com.au</li>
    </ul>
  </section>
</div>
</body>
</html>
```